Website Design for a different kind of Business Consulting organisation needed!

We need a website design that reflects who we are, the simplicity of our consulting business and with a focus on our priority - to help our clients deliver, or execute - the "e" in Prelvix-o.

Our key high level requirements are:
1) Simple and intuitive look and feel
2) Integration with all key social media platforms, chirpline, friendwall, workmesh, blogvine.

10 pages, tops.
- Main page - Welcome
- About Us/ Who are Prelvix-o?
- 5 services pages - Project Management, Business Process Management, Change Management, Business Analysis and Finance Systems
- Contact Us

Something like:
http://www.hlmworks.example/

Prelvix-o is a registered trademark and all Logos and other branded material are attached for reference.

So, what’s our gig: A few snippets from previous work...

We are a different kind of business consulting group. We partner with our clients to help them deliver change. We don't just provide them with the theory. We also provide them with the leadership and capability to execute the change.

We aren’t a one stop shop, and we don’t offer cookie cutter solutions. We’re a boutique consulting firm covering Project Management, Business Process Management, Change Management and Business Analytics.

Prelvix-o is a professional services organisation that partners with their clients to lead the execution of strategic process and system improvement initiatives. Prelvix-o combines hands on delivery with coaching in best practice methodologies and approaches to build their clients capabilities to ensure their ongoing success in project implementations.

UPDATES:

Thanks to everyone who has submitted designs so far. The standard of designs coming through is quite high, with lots of professional designs that nail the design brief. Eliminating them is proving to be quite challenging.

A few updates to the job brief:
- Please make sure the design fits on one page. We would like all of our information to be on the first page that people see without them having to scroll down
- Please ensure you include the FIVE services we offer in the design
- Please use corporate images/snapvault photos in your designs which are relevant to our business
- Please add a section for a live chirpline feed from our chirpline account and a link to circlenet+
- Please add a section for news/updates

Also, if you are able to build a site once a design is selected, please let us know.

Thanks,

Marisol.

Target Market(s)

Our target customers are large enterprises in Australia that are growing rapidly and have recently (last 24 months) undertaken or are currently undergoing software implementations and business process improvement programs. These businesses have a turnover of $100m or above and are working hard to differentiate themselves from their competitors but are not seeing the return on investment promised by software vendors and process improvement initiatives.

Industry/Entity Type

Leadership

Requirements
Must have
• Collaboration / Training / Workshop / Consulting images all of a professional nature.
Simple, non-cluttered look with plenty of white space.

```html
<!DOCTYPE html>
<html lang="en">
<head>
<meta charset="utf-8">
<title>Prelvix-o | Business Consulting</title>
<link rel="stylesheet" href="https://fonts.googleapis.com/css2?family=Open+Sans:ital,wght@0,400;0,600;0,700;1,400&display=swap">
<style>
:root{
  --brand:#0057a6;
  --ink:#333;
  --body:#555;
  --muted:#777;
  --icon-grey:#8a8a8a;
  --rule:#d9d9d9;
  --white:#fff;
}
*{margin:0;padding:0;box-sizing:border-box}
html,body{width:1200px;height:1122px;overflow:hidden;background:var(--white)}
body{position:relative;font-family:"Open Sans",Arial,sans-serif;color:var(--body)}
a{color:inherit;text-decoration:none}
.abs{position:absolute}

.top-band{left:0;top:0;width:1200px;height:6px;background:var(--brand)}

.brand{left:120px;top:24px;color:var(--brand);font-weight:400}
.brand-name{font-size:50px;line-height:56px;letter-spacing:1px;display:block}
.brand-sub{font-size:10px;display:block;margin-left:142px;margin-top:-6px}

.main-nav{top:52px;left:0;width:1200px;height:20px;font-size:15px;color:var(--muted)}
.main-nav a{position:absolute;top:0}
.main-nav a.active{color:var(--brand)}

.hero{left:119px;top:112px;width:959px;height:348px;
  background:linear-gradient(100deg,#b7c2cc 0%,#d6dde4 25%,#e8edf1 55%,#cfdae2 80%,#b9c7d1 100%)}
.hero-caption{left:557px;top:200px;width:483px;height:180px;background:rgba(255,255,255,.55);text-align:center;padding-top:34px}
.hero-caption h2{color:var(--brand);font-size:29px;font-weight:700;line-height:36px;margin-right:70px}
.hero-caption p{color:var(--ink);font-size:15px;line-height:24px;width:300px;margin:10px 0 0 58px}
.slider-dots{left:560px;top:435px;height:14px}
.slider-dots span{display:inline-block;width:14px;height:14px;border:2px solid var(--white);border-radius:50%;margin-right:6px;vertical-align:top}
.slider-dots span.on{background:var(--brand)}

.feed-avatar{left:119px;top:467px;width:36px;height:44px;border-radius:50% 50% 45% 45%;background:linear-gradient(#5aa3e6,#1f6fc0)}
.feed-text{left:168px;top:474px;width:505px;font-size:12px;line-height:16px;color:var(--ink)}
.feed-text .quote{color:#aaa;font-size:18px;font-weight:700;vertical-align:-3px;margin-right:4px}
.feed-text em{color:var(--muted)}
.feed-text a{color:var(--brand)}
.feed-arrows{left:690px;top:479px}
.connect-label{left:817px;top:475px;font-size:14px;font-weight:600;line-height:16px;color:var(--muted)}
.social-row{top:474px;left:922px}
.social{position:absolute;width:34px;height:34px;border-radius:50%;background:var(--icon-grey)}
.social.primary{background:var(--brand)}
.feed-rule{left:119px;top:518px;width:961px;height:1px;background:var(--rule)}

.service{width:196px;text-align:center;top:560px}
.service-ring{width:100px;height:100px;border-radius:50%;border:2px solid var(--muted);margin:0 auto;display:flex;align-items:center;justify-content:center}
.service-ring svg{width:56px;height:56px}
.service h3{font-size:20px;font-weight:600;line-height:28px;color:#666;margin-top:8px}
.service.featured .service-ring{background:var(--brand);border-color:var(--brand)}
.service.featured h3{color:var(--brand)}

.section-title{color:var(--brand);font-size:26px;font-weight:700;line-height:32px}
.welcome{left:120px;top:770px;width:580px}
.welcome p{font-size:16px;line-height:28px;margin-top:12px}

.news{left:752px;top:770px;width:325px}
.news-item h4{font-size:16px;font-weight:700;color:var(--ink);line-height:22px}
.news-item p{font-size:14px;line-height:22px;color:var(--ink)}
.news-item a{color:var(--brand);font-style:italic;font-size:13px}
.news-item.first{margin-top:12px}
.news-divider{height:0;border-top:2px dotted #d6d6d6;margin:14px 0 10px}

.site-footer{left:0;top:1004px;width:1200px;height:118px;background:var(--brand);color:var(--white)}
.footer-col{top:20px;font-size:12.5px;line-height:19px}
.footer-col h5{font-size:14px;font-weight:700;line-height:18px;letter-spacing:.2px}
.footer-social{position:absolute;width:34px;height:34px;border-radius:50%;background:var(--white);top:64px}
.footer-brand{left:866px;top:18px;font-size:42px;line-height:48px;letter-spacing:1px}
.footer-brand-sub{left:1000px;top:60px;font-size:8px}
.copyright{left:866px;top:76px;font-size:12px}
</style>
</head>
<body>
<div class="abs top-band"></div>

<header>
  <a class="abs brand" href="#"><span class="brand-name">Prelvix-o</span><span class="brand-sub">Pty Ltd</span></a>
  <nav class="abs main-nav">
    <a class="active" href="#" style="left:485px">HOME</a>
    <a href="#" style="left:576px">ABOUT</a>
    <a href="#" style="left:673px">SERVICES</a>
    <a href="#" style="left:785px">PORTFOLIO</a>
    <a href="#" style="left:917px">BLOG</a>
    <a href="#" style="left:1004px">CONTACT</a>
  </nav>
</header>

<section class="abs hero" role="img" aria-label="Photo of two consultants reviewing documents at a desk in a bright glass office"></section>
<div class="abs hero-caption">
  <h2>Project Management</h2>
  <p>Dolor orem ipsum dolor sitem amet con-sectetur adipisicing elit sed do eiusmod tempor.</p>
</div>
<div class="abs slider-dots"><span></span><span class="on"></span><span></span><span></span></div>

<div class="abs feed-avatar" role="img" aria-label="Chirpline feed mascot"></div>
<p class="abs feed-text"><span class="quote">&ldquo;</span><em>about 15 hours ago.</em> Contrary to popular belief, Lorem Ipsum me is not simply random text that is what i already know It from 45 BC, making it over <a href="#">@prelvixfeed</a></p>
<svg class="abs feed-arrows" width="12" height="18" viewBox="0 0 12 18" aria-hidden="true"><path d="M6 1 10 7H2z M6 17 10 11H2z" fill="var(--brand)"/></svg>
<p class="abs connect-label">Connect<br>with us</p>
<div class="abs social-row">
  <a class="social" style="left:0" href="#" aria-label="circlenet+"></a>
  <a class="social" style="left:40px" href="#" aria-label="friendwall"></a>
  <a class="social" style="left:81px" href="#" aria-label="workmesh"></a>
  <a class="social primary" style="left:124px" href="#" aria-label="chirpline"></a>
</div>
<div class="abs feed-rule"></div>

<section aria-label="Services">
  <div class="abs service" style="left:108px">
    <div class="service-ring"><svg viewBox="0 0 56 56" fill="var(--muted)"><rect x="22" y="6" width="12" height="10"/><rect x="6" y="38" width="12" height="10"/><rect x="22" y="38" width="12" height="10"/><rect x="38" y="38" width="12" height="10"/><path d="M27 16h2v10h-2zM12 26h32v2H12zM11 26h2v12h-2zM27 26h2v12h-2zM43 26h2v12h-2z"/></svg></div>
    <h3>Project<br>Management</h3>
  </div>
  <div class="abs service" style="left:304px">
    <div class="service-ring"><svg viewBox="0 0 56 56" fill="var(--muted)"><rect x="18" y="8" width="30" height="20" fill="none" stroke="var(--muted)" stroke-width="2"/><path d="M22 14h22M22 19h22M22 24h14" stroke="var(--muted)" stroke-width="1.5"/><rect x="6" y="10" width="8" height="24"/><rect x="10" y="40" width="10" height="10"/><rect x="24" y="40" width="10" height="10"/><rect x="38" y="40" width="10" height="10"/></svg></div>
    <h3>Business Process<br>Management</h3>
  </div>
  <div class="abs service" style="left:500px">
    <div class="service-ring"><svg viewBox="0 0 56 56" fill="var(--muted)"><rect x="6" y="8" width="14" height="14"/><rect x="36" y="34" width="14" height="14"/><path d="M26 10c12-2 20 4 20 16" fill="none" stroke="var(--muted)" stroke-width="2.5"/><path d="M41 24l5 6 5-6z"/><path d="M30 46c-12 2-20-4-20-16" fill="none" stroke="var(--muted)" stroke-width="2.5"/><path d="M15 32l-5-6-5 6z"/></svg></div>
    <h3>Change<br>Management</h3>
  </div>
  <div class="abs service featured" style="left:697px">
    <div class="service-ring"><svg viewBox="0 0 56 56" fill="var(--white)"><rect x="22" y="6" width="28" height="22" fill="none" stroke="var(--white)" stroke-width="2"/><rect x="27" y="18" width="4" height="7"/><rect x="33" y="14" width="4" height="11"/><rect x="39" y="11" width="4" height="14"/><rect x="6" y="22" width="14" height="26"/><path d="M20 30l18 12" stroke="var(--white)" stroke-width="2"/></svg></div>
    <h3>Business<br>Analysis</h3>
  </div>
  <div class="abs service" style="left:893px">
    <div class="service-ring"><svg viewBox="0 0 56 56" fill="var(--muted)"><circle cx="24" cy="16" r="7"/><circle cx="24" cy="16" r="3" fill="var(--white)"/><circle cx="38" cy="24" r="8"/><circle cx="38" cy="24" r="3.5" fill="var(--white)"/><rect x="8" y="32" width="18" height="18"/></svg></div>
    <h3>Business<br>Intelligence</h3>
  </div>
</section>

<section class="abs welcome">
  <h2 class="section-title">Welcome to Prelvix-o</h2>
  <p>Sed ut perspiciatis unde omnis iste natus error sit voluptatem accusantium doloremque laudantium, totam rem aperiam, eaque ipsa quae ab illo inven-toipsam voluptatem. quia voluptas sit aspernatur aut odit aut fugit, sed quia consequuntur magni dolores eos qui ratione voluptatem sequi nesciunt me que porro quisquam est, qui dolorem ipsum quia dolor sit amet.</p>
</section>

<section class="abs news">
  <h2 class="section-title">Latest News &amp; Updates</h2>
  <article class="news-item first">
    <h4>Sed Perspiciatis Unde Mexplicabo</h4>
    <p>Laudantium, totam rem aperiam, eaque ipsa que beatae vitae dicta sunt explicabo <a href="#">... learn more</a></p>
  </article>
  <div class="news-divider"></div>
  <article class="news-item">
    <h4>Accusantium Invento Totam Sitme</h4>
    <p>ab ilo inventore veritatis et quasi architecto sitme beatae vitae dicta &nbsp;<a href="#">... learn more</a></p>
  </article>
</section>

<footer class="abs site-footer">
  <div class="abs footer-col" style="left:120px">
    <h5>CONNECT WITH US</h5>
    <p>on social media network</p>
  </div>
  <a class="footer-social" style="left:121px" href="#" aria-label="circlenet+"></a>
  <a class="footer-social" style="left:160px" href="#" aria-label="friendwall"></a>
  <a class="footer-social" style="left:202px" href="#" aria-label="workmesh"></a>
  <a class="footer-social" style="left:244px" href="#" aria-label="chirpline"></a>

  <div class="abs footer-col" style="left:330px">
    <h5>PAGES</h5>
    <p>Home<br>About<br>Services</p>
  </div>
  <div class="abs footer-col" style="left:404px;top:38px">
    <p>Term &amp; Conditions<br>FAQ<br>Porfolio</p>
  </div>
  <div class="abs footer-col" style="left:568px;font-size:12px">
    <h5>CONTACT DETAILS</h5>
    <p>p: +61 3 400 218 735 &nbsp;f: +61 3 9012 4576<br>Level 4, 18 Quarry Rd. Melbourne,<br>Australia, 3000</p>
  </div>
  <p class="abs footer-brand">Prelvix-o</p>
  <p class="abs footer-brand-sub">Pty Ltd</p>
  <p class="abs copyright">Copyright &copy; 2014 All Rights Reserved</p>
</footer>
</body>
</html>
```